Company brochure for our unique consulting business

We are a small consulting business offering a unique set of services to our clients.. In simple terms we are a business improvement consultancy helping our clients get the best out of their businesses. We work with clients across multiple sectors and deliver a variety of services. We want to put together a brochure to cover these main themes:1. Who we are2. What we do3. The type of people we employ4. The sectors we work inWhile the brochure needs to have a certain corporate feel to it, we don't want it to be "boring" or "stiff". We would like it to have a slightly "friendly" or "informal" feel to it, to reflect the type of organisation we are.We have a company website http://tollandvergeadvisory.com , however we do not want to directly replicate the content or feel as we recognise it needs updating.We would like the brochure to be A4 portrait format. We anticipate requiring 12 sides (including covers) but we are happy to be guided on this based on the content we have provided.The attached ppt file gives the detail of the content to be included and also shows the proposed pagination. For the front cover we would like to try 2 versions, one with the TVA logo and one with the Tolland Verge Advisory logo (a file of both is attached)One of the most important pages will be the "Our Services" page. We would like this to cover the centre fold. In the ppt file we have shown an example layout, but this is where we need most help - we are clearly not graphic designers! This page will be the most used page in sales meetings etc.Also attached is the following:1. file for our TollandVerge Advisory company logo.2. File for our TVA company logo3. Files for Derek's signatures (for under photos) - Owen's to follow4. Photo of Derek & Owen (person in purple shirt to be cropped out)Thank you and really excited to see what everyone comes back with.Derek & Owen

Target Market(s)

Very broad - Manufacturing, Healthcare, Hospitality

Industry/Entity Type

Management Consulting

Font styles to use
Other font styles liked:
• We use Swiss721, but happy to be guided by designer

Colors
3276b5
85abd2
0355a3
333333
5c5c5c
9d9d9d
d9d9d9

Requirements
Must have
• Corporate feel
Nice to have
• Slightly friendly feel
• Our standard "blue" is (CORRECTION) - R55 G96 B146 #376092 and our standard grey is R197 G178, B179 - #B3B2B2, which we would like to keep, but other colours we are happy to be guided on. Brand guidelines attached.

```html
<!DOCTYPE html>
<html lang="en">
<head>
<meta charset="utf-8">
<title>Tolland Verge Advisory – Brochure Cover Spread</title>
<link rel="stylesheet" href="https://fonts.googleapis.com/css2?family=Arimo:wght@400;700&display=swap">
<style>
  :root {
    --backdrop: #e4e4e4;
    --page-white: #ffffff;
    --steel-grey: #939396;
    --pale-grey: #c4c4c6;
    --shadow-grey: #5c5c5c;
    --brand-blue: #376092;
    --bright-blue: #0062b0;
    --light-blue: #4a95d0;
    --ink: #111111;
    --text-grey: #555555;
  }
  html, body {
    margin: 0;
    width: 1200px;
    height: 1200px;
    overflow: hidden;
    background: var(--backdrop);
  }
  .spread {
    position: absolute;
    left: 29px;
    top: 197px;
    width: 1142px;
    height: 806px;
    display: block;
  }
  .tagline { font-family: "Arimo", Arial, sans-serif; font-size: 24px; fill: var(--text-grey); }
  .tagline-accent { font-weight: 700; fill: var(--brand-blue); }
  .wordmark { font-family: "Arimo", Arial, sans-serif; font-weight: 700; fill: var(--ink); }
  .web-address { font-family: "Arimo", Arial, sans-serif; font-size: 17px; fill: var(--text-grey); }
</style>
</head>
<body>
<svg class="spread" viewBox="40 203 1428 1008" xmlns="http://www.w3.org/2000/svg">
  <defs>
    <linearGradient id="mono-glass" x1="0" y1="0" x2="1" y2="1">
      <stop offset="0" stop-color="#d8dadc"/>
      <stop offset="0.5" stop-color="#6f767c"/>
      <stop offset="1" stop-color="#2f363c"/>
    </linearGradient>
    <linearGradient id="sky-tower" x1="0" y1="0" x2="1" y2="1">
      <stop offset="0" stop-color="#9fb8e0"/>
      <stop offset="0.55" stop-color="#3f5a82"/>
      <stop offset="1" stop-color="#222c3a"/>
    </linearGradient>
    <linearGradient id="blue-fade" x1="0" y1="0" x2="1" y2="0">
      <stop offset="0" stop-color="var(--light-blue)"/>
      <stop offset="0.6" stop-color="var(--bright-blue)"/>
    </linearGradient>
    <linearGradient id="spine-shade-back" x1="0" y1="0" x2="1" y2="0">
      <stop offset="0" stop-color="#ffffff" stop-opacity="0"/>
      <stop offset="0.55" stop-color="#ffffff" stop-opacity="0"/>
      <stop offset="1" stop-color="#000000" stop-opacity="0.28"/>
    </linearGradient>
    <linearGradient id="network-field" x1="0" y1="0" x2="1" y2="0">
      <stop offset="0" stop-color="var(--pale-grey)"/>
      <stop offset="0.12" stop-color="var(--steel-grey)"/>
      <stop offset="1" stop-color="var(--steel-grey)"/>
    </linearGradient>
    <radialGradient id="network-glow" cx="0.55" cy="0.5" r="0.6">
      <stop offset="0" stop-color="#ffffff" stop-opacity="0.22"/>
      <stop offset="1" stop-color="#ffffff" stop-opacity="0"/>
    </radialGradient>
  </defs>

  <!-- Back cover -->
  <g class="back-cover">
    <rect x="40" y="203" width="714" height="1008" fill="var(--page-white)"/>
    <rect x="40" y="203" width="714" height="469" fill="var(--steel-grey)"/>
    <rect x="40" y="672" width="714" height="371" fill="url(#mono-glass)" role="img" aria-label="Photograph looking up between glass office towers, black and white"/>
    <rect x="40" y="203" width="714" height="1008" fill="url(#spine-shade-back)"/>
    <polygon points="252,631 292,672 252,672" fill="var(--shadow-grey)"/>
    <polygon points="70,1043 110,1083 110,1043" fill="var(--shadow-grey)"/>
    <polygon points="90,631 252,631 252,885 90,728" fill="var(--bright-blue)"/>
    <polygon points="110,760 352,1000 352,1083 110,1083" fill="var(--brand-blue)"/>
    <text class="tagline" x="367" y="1076">helping businesses <tspan class="tagline-accent">evolve</tspan></text>
    <text class="wordmark" x="108" y="1148" font-size="40">TVA</text>
    <text class="web-address" x="108" y="1172">www.tollandvergegroup.com</text>
  </g>

  <!-- Front cover -->
  <g class="front-cover">
    <rect x="754" y="203" width="714" height="1008" fill="var(--page-white)"/>
    <g role="img" aria-label="Decorative network of connected dots in white on grey">
      <rect x="754" y="765" width="714" height="446" fill="url(#network-field)"/>
      <rect x="754" y="765" width="714" height="446" fill="url(#network-glow)"/>
    </g>
    <polygon points="755,288 1028,288 755,765" fill="url(#blue-fade)"/>
    <polygon points="1028,288 1090,392 968,392" fill="var(--steel-grey)"/>
    <polygon points="968,392 1467,392 1467,450 1283,765 755,765" fill="url(#sky-tower)" role="img" aria-label="Photograph of glass skyscrapers against a blue sky"/>
    <polygon points="1163,765 1283,765 1223,868" fill="var(--shadow-grey)"/>
    <polygon points="1467,450 1467,868 1223,868" fill="var(--brand-blue)"/>
    <text class="wordmark" x="1422" y="340" font-size="58" text-anchor="end">TVA</text>
    <text class="tagline" x="1422" y="373" text-anchor="end">helping businesses <tspan class="tagline-accent">evolve</tspan></text>
  </g>
</svg>
</body>
</html>
```